Elegant Black Candle Label Design!

I need a 2.375" tall by 3.0" wide candle label design. I'm looking for simple and elegant. Black label with silver leaf border and lettering. Label needs to have the following information on it: Fern Hollow Candle Co. as the company name, scent name in the middle and in smaller font, it needs to say Made in USA, All Natural, 8oz. Attached photos are for inspiration.

Target Market(s)

People looking for high end, all natural candle fragrances

Industry/Entity Type

Candle-Spa

Colors

Designer to choose only greyscale colors for use in the design.

Requirements
Must have
• Company Name, Scent (ability to change scent names), All Natural, Made in USA, 8oz
Nice to have
• Black background, silver leaf border and silver leaf font. Elegant fonts maybe slightly cursive

```html
<!DOCTYPE html>
<html lang="en">
<head>
<meta charset="utf-8">
<title>Fern Hollow Candle Co. – Lavender Label</title>
<link href="https://fonts.googleapis.com/css2?family=Josefin+Sans:wght@300&family=Bodoni+Moda:wght@400&display=swap" rel="stylesheet">
<style>
  :root {
    --ink: #000000;
    --silver: #d4d4d4;
    --silver-light: #f4f4f4;
    --silver-mid: #c2c2c2;
    --text-silver: #e6e6e6;
    --white: #ffffff;
  }
  html, body {
    margin: 0;
    padding: 0;
    width: 1200px;
    height: 1200px;
    overflow: hidden;
    background: var(--ink);
  }
  .canvas {
    position: relative;
    width: 1200px;
    height: 1200px;
    background: var(--ink);
    font-family: "Josefin Sans", sans-serif;
    font-weight: 300;
    color: var(--text-silver);
  }
  .label {
    position: absolute;
    left: 302px;
    top: 265px;
    width: 596px;
    height: 670px;
    box-sizing: border-box;
    border: 9px solid var(--silver);
    border-radius: 46px;
  }
  .brand-dot {
    position: absolute;
    left: 569px;
    top: 335px;
    width: 62px;
    height: 62px;
    box-sizing: border-box;
    border: 1.5px solid var(--text-silver);
    border-radius: 50%;
  }
  .brand-name {
    position: absolute;
    left: 0;
    top: 448px;
    width: 1200px;
    text-align: center;
    font-size: 34px;
    letter-spacing: 2px;
    color: var(--text-silver);
  }
  .scent-plate {
    position: absolute;
    left: 430px;
    top: 593px;
    width: 340px;
    height: 72px;
  }
  .scent-name {
    position: absolute;
    left: 430px;
    top: 593px;
    width: 340px;
    height: 72px;
    line-height: 76px;
    text-align: center;
    font-family: "Bodoni Moda", serif;
    font-size: 42px;
    letter-spacing: -1px;
    color: var(--ink);
  }
  .detail {
    position: absolute;
    font-size: 21px;
    letter-spacing: 0.5px;
    color: var(--text-silver);
    white-space: nowrap;
  }
  .detail--origin { left: 373px; top: 856px; }
  .detail--natural {
    right: 372px;
    top: 808px;
    padding-bottom: 9px;
    border-bottom: 2px solid var(--text-silver);
  }
  .detail--weight { right: 372px; top: 856px; }
</style>
</head>
<body>
<main class="canvas">
  <div class="label"></div>

  <div class="brand-dot"></div>
  <div class="brand-name">Fern Hollow Candle Co.</div>

  <svg class="scent-plate" viewBox="0 0 340 72" aria-hidden="true">
    <defs>
      <linearGradient id="plateSheen" x1="0" y1="0" x2="1" y2="1">
        <stop offset="0" stop-color="#b8b8b8"/>
        <stop offset="0.35" stop-color="#f7f7f7"/>
        <stop offset="0.6" stop-color="#d9d9d9"/>
        <stop offset="1" stop-color="#bdbdbd"/>
      </linearGradient>
    </defs>
    <rect x="1" y="1" width="338" height="70" rx="16" fill="var(--silver-light)"/>
    <rect x="5" y="5" width="330" height="62" rx="13" fill="var(--ink)"/>
    <rect x="8" y="8" width="324" height="56" rx="11" fill="url(#plateSheen)"/>
  </svg>
  <div class="scent-name">LAVENDER</div>

  <div class="detail detail--natural">All Natural</div>
  <div class="detail detail--origin">Made in USA</div>
  <div class="detail detail--weight">8oz</div>
</main>
</body>
</html>
```